UI Design & Web Design for Used Car Dealer.
Modern and user friendly responsive layout for mobiles and desktop. Bootstrap and form elements for members,registration process,login,dashboard. Layouts for Home Page, Car Listing Pages, Individual Car Information page and etc.

Output files in Bootstrap Html/CSS
Please refer to attachments for more details.

Target Market(s)

Asia / Singapore

Industry/Entity Type

Car Dealer

Coding

Coded - Design and coding required

Number of Pages Required

5+ page

Font styles to use
Sans Serif

Colors
acd037
f6faec
cfcfcf
b1b1b1
ffffff

Requirements
Must have
• Coded in Bootstrap 3 UI Elements, Forms, Labels, Sections, Tables, Buttons, Alerts, Modal, Fonts, Dashboard, Login, Register,Contact
Nice to have
• Stock Images
Should not have
• NA

```html
<!DOCTYPE html>
<html lang="en">
<head>
<meta charset="utf-8">
<title>Drivemarq – Home</title>
<link href="https://fonts.googleapis.com/css2?family=Exo+2:wght@300;400;500;600;700&display=swap" rel="stylesheet">
<style>
  :root {
    --green: #6cbf3f;
    --green-soft: #acd037;
    --ink: #222222;
    --grey-text: #6b6b6b;
    --grey-line: #cfcfcf;
    --footer-bg: #d2d2d2;
    --white: #ffffff;
    --hero-dark: #151a26;
    --hero-mid: #3a4354;
  }
  * { box-sizing: border-box; margin: 0; padding: 0; }
  html, body { width: 1200px; height: 1200px; overflow: hidden; }
  body {
    position: relative;
    font-family: "Exo 2", sans-serif;
    background: var(--white);
    color: var(--ink);
  }

  /* Header */
  .site-header {
    position: absolute; left: 0; top: 0; width: 1200px; height: 52px;
    background: var(--white);
  }
  .brand {
    position: absolute; left: 186px; top: 14px;
    display: flex; align-items: center; gap: 10px;
  }
  .brand-square { width: 40px; height: 31px; background: var(--green); border-radius: 3px; }
  .brand-name {
    font-size: 22px; font-weight: 600; color: var(--green);
    letter-spacing: 1px; text-transform: uppercase;
  }
  .main-nav {
    position: absolute; top: 18px; left: 569px;
    display: flex; gap: 0;
    font-size: 11.5px; text-transform: uppercase; color: #333;
  }
  .main-nav a { color: inherit; text-decoration: none; position: absolute; white-space: nowrap; }
  .main-nav .is-active { color: var(--green); font-weight: 700; font-size: 13px; top: -1px; }

  /* Hero */
  .hero {
    position: absolute; left: 0; top: 52px; width: 1200px; height: 578px;
    background: radial-gradient(ellipse at 50% 45%, #5a6476 0%, var(--hero-mid) 35%, var(--hero-dark) 100%);
    color: var(--white);
  }
  .hero-photo {
    position: absolute; left: 265px; top: 90px; width: 650px; height: 360px;
    background: radial-gradient(ellipse at 50% 55%, #8a93a3 0%, #5a6374 45%, rgba(40,46,60,0) 75%);
  }
  .hero-title {
    position: absolute; left: 188px; top: 400px;
    font-size: 47px; font-weight: 400; letter-spacing: -0.5px; text-transform: uppercase;
  }
  .hero-rule {
    position: absolute; left: 188px; top: 485px; width: 569px; height: 1px;
    background: #4f6a3a;
  }
  .hero-text {
    position: absolute; left: 192px; top: 500px; width: 840px;
    font-size: 18px; line-height: 23.5px; font-weight: 400;
  }

  /* Intro */
  .intro {
    position: absolute; left: 0; top: 630px; width: 1200px; height: 496px;
    background: linear-gradient(#e9e9e9 0%, #f6f6f6 8%, var(--white) 60%);
  }
  .intro-kicker {
    position: absolute; left: 188px; top: 62px;
    font-size: 19px; font-weight: 300; color: #555;
  }
  .intro-title {
    position: absolute; left: 186px; top: 82px;
    font-size: 62px; font-weight: 400; color: var(--green); letter-spacing: -0.5px;
  }
  .intro-tagline {
    position: absolute; left: 188px; top: 152px;
    font-size: 15px; font-weight: 300; color: var(--grey-text);
  }
  .intro-rule {
    position: absolute; left: 188px; top: 224px; width: 832px; height: 1px;
    background: var(--grey-line);
  }
  .side-photo {
    position: absolute; left: 1008px; top: 140px; width: 192px; height: 356px;
    background: radial-gradient(ellipse at 80% 50%, #2a2a2a 0%, #8d8d8d 40%, rgba(255,255,255,0) 72%);
  }

  .feature { position: absolute; top: 274px; width: 240px; }
  .feature-title {
    font-size: 19px; font-weight: 400; color: #333; text-transform: uppercase;
    padding-bottom: 6px; position: relative;
  }
  .feature-title::after {
    content: ""; position: absolute; left: 0; bottom: -3px; width: 78px; height: 3px;
    background: var(--green);
  }
  .feature-text {
    margin-top: 14px; font-size: 12px; line-height: 16px; font-weight: 400; color: #555;
  }
  .btn-more {
    position: absolute; top: 106px; left: 0;
    width: 81px; height: 25px; line-height: 25px; text-align: center;
    background: var(--green); color: var(--white);
    font-size: 10px; font-weight: 700; text-transform: uppercase; border-radius: 2px;
  }

  /* Footer */
  .site-footer {
    position: absolute; left: 0; top: 1126px; width: 1200px; height: 74px;
    background: var(--footer-bg); font-size: 10.5px; color: #444;
  }
  .footer-links { position: absolute; left: 120px; top: 31px; }
  .footer-copy { position: absolute; right: 106px; top: 31px; }
</style>
</head>
<body>
  <header class="site-header">
    <div class="brand">
      <span class="brand-square"></span>
      <span class="brand-name">Drivemarq</span>
    </div>
    <nav class="main-nav">
      <a class="is-active" style="left:0">Home</a>
      <a style="left:63px">Benefits</a>
      <a style="left:133px">Vehicle Listings</a>
      <a style="left:245px">Start Advertising Now</a>
      <a style="left:402px">Contact</a>
    </nav>
  </header>

  <section class="hero">
    <div class="hero-photo" role="img" aria-label="Grey sports coupe on a dark misty studio floor"></div>
    <h1 class="hero-title">We’ve got it arranged</h1>
    <div class="hero-rule"></div>
    <p class="hero-text">Drivemarq.com is an online platform which covers every single aspects from buying to selling of your vehicles. From engagement of a Servicing Agent till successfully handing over its ownership through a smarter and secure solutions</p>
  </section>

  <section class="intro">
    <p class="intro-kicker">With Drivemarq.com platform</p>
    <h2 class="intro-title">THE MARGIN IS YOURS</h2>
    <p class="intro-tagline">when you reaches out to potential vehicle enthusiasts directly.</p>
    <div class="intro-rule"></div>
    <div class="side-photo" role="img" aria-label="Glossy black car seen from the side, partly cropped"></div>

    <article class="feature" style="left:189px">
      <h3 class="feature-title">Advertise Now</h3>
      <p class="feature-text">Upload images and vehicle details right after creating an account which is absolutely hassle &amp; cost free.</p>
      <span class="btn-more">Read More</span>
    </article>
    <article class="feature" style="left:487px">
      <h3 class="feature-title">Promote Your Business</h3>
      <p class="feature-text">Leverage our busy online traffic which makes us an excellent business platform for limitless exposure.</p>
      <span class="btn-more">Read More</span>
    </article>
    <article class="feature" style="left:786px">
      <h3 class="feature-title">Online Insurance</h3>
      <p class="feature-text">Fill up your details on one form, we will provide several quotation to suits your requirement.</p>
      <span class="btn-more">Read More</span>
    </article>
  </section>

  <footer class="site-footer">
    <div class="footer-links">Home &nbsp;|&nbsp; Privacy &nbsp;|&nbsp; Terms and Conditions &nbsp;|&nbsp; Contact us</div>
    <div class="footer-copy">Copyright © 2016. All Right Reserved</div>
  </footer>
</body>
</html>
```